New Email Marketing Design Project

I’d like you to make an email template. I’ll be welcoming and on boarding customers via email. And I’d like the branding to stand out. Keep it professional and simple. But be creative.

Design should look amazing on desktop and mobile phones.

Negative white space is ok.

Use stock images

I’ll like to have a spot for a picture of myself so make sure to include a circle where I can show my face so that email viewers will know who is speaking to them.

Target Market(s)

Practice managers, doctors, medical providers

Font styles to use
Sans Serif

Requirements
Must have
• Our Logo, CTA buttons, Same colors as website.
https://www.tavrenhealthclaims.com

```html
<!DOCTYPE html>
<html lang="en">
<head>
<meta charset="utf-8">
<title>Tavren Health Claims – Welcome Email</title>
<link href="https://fonts.googleapis.com/css2?family=Montserrat:wght@400;500;700&display=swap" rel="stylesheet">
<style>
:root{
  --page-bg:#f8f8f8;
  --sheet:#ffffff;
  --brand:#2f78a0;
  --brand-dark:#2a6e94;
  --text:#1f1f1f;
  --muted:#9a9a9a;
  --placeholder:#f3f3f3;
  --placeholder-text:#c4c4c4;
  --card:#f9f9f9;
}
*{box-sizing:border-box;margin:0;padding:0}
html,body{width:1200px;height:3037px;overflow:hidden}
body{background:var(--page-bg);font-family:"Montserrat",sans-serif;color:var(--text);position:relative}
.view-online{position:absolute;top:60px;left:0;width:1200px;text-align:center;font-size:19px;color:#8a8a8a}
.sheet{position:absolute;top:125px;left:80px;width:1040px;height:2531px;background:var(--sheet)}
.header{height:200px;position:relative}
.brand{position:absolute;left:45px;top:40px;display:flex;align-items:center;gap:26px}
.brand-mark{width:112px;height:112px;border-radius:50%;border:4px solid var(--brand)}
.brand-name{font-weight:700;font-size:30px;line-height:42px;color:var(--brand);width:290px}
.phone{position:absolute;right:48px;top:89px;display:flex;align-items:center;gap:16px;font-weight:700;font-size:28px;color:var(--brand);letter-spacing:-.5px}
.phone svg{width:62px;height:62px}
.hero{height:281px;background:linear-gradient(100deg,#efe9ef 0%,#f4eef4 45%,#dfe8f0 70%,#b9d6ea 100%)}
.greeting{position:relative;padding:50px 48px 0}
.greeting h1{font-size:39px;font-weight:700;color:var(--brand);line-height:50px}
.greeting p{width:660px;margin-top:20px;font-size:23px;line-height:38.4px}
.avatar{position:absolute;left:807px;top:58px;width:182px;height:182px;border-radius:50%;background:var(--placeholder);display:flex;align-items:center;justify-content:center;color:var(--placeholder-text);font-size:36px}
.cards{position:absolute;left:48px;top:781px;width:944px;display:grid;grid-template-columns:451px 451px;column-gap:42px;row-gap:38px}
.card{background:var(--card);height:680px}
.card-image{height:227px;background:var(--placeholder);display:flex;align-items:center;justify-content:center;color:var(--placeholder-text);font-size:36px}
.card-body{padding:38px 48px 0}
.card-body h2{font-size:38px;font-weight:700;color:var(--brand);line-height:48px}
.card-body p{margin-top:18px;font-size:23px;line-height:38.4px}
.button{display:inline-block;margin-top:27px;width:208px;height:77px;line-height:77px;text-align:center;background:var(--brand);color:#fff;font-weight:700;font-size:25px;border-radius:6px;text-decoration:none}
.closing{position:absolute;left:48px;top:2226px;width:944px}
.closing h2{font-size:38px;font-weight:700;color:var(--brand);line-height:48px}
.closing p{margin-top:20px;font-size:23px;line-height:38.4px}
.footer{position:absolute;top:2700px;left:80px;width:1040px}
.footer-brand{display:flex;align-items:center;gap:18px}
.footer-mark{width:74px;height:74px;border-radius:50%;border:3px solid #c8c8c8}
.footer-name{font-weight:700;font-size:30px;line-height:42px;color:#b5b5b5;width:290px}
.social{position:absolute;right:0;top:27px;display:flex;gap:17px}
.social span{width:56px;height:56px;border-radius:50%;border:3px solid #a8a8a8}
.footer-text{margin-top:42px;font-size:19px;line-height:34px;color:var(--muted)}
.unsubscribe{display:block;margin-top:17px;font-size:19px;color:#8a8a8a;text-decoration:none}
</style>
</head>
<body>
<div class="view-online">View online version</div>
<main class="sheet">
  <header class="header">
    <div class="brand">
      <span class="brand-mark"></span>
      <span class="brand-name">Tavren Health Claims</span>
    </div>
    <div class="phone">
      <svg viewBox="0 0 62 62" aria-hidden="true">
        <circle cx="31" cy="31" r="28.5" fill="none" stroke="#2f78a0" stroke-width="4"/>
        <path d="M22 17c2-1 3 0 4 1l4 6c1 2 0 3-1 4l-2 2c1 3 5 7 8 8l2-2c1-1 2-2 4-1l6 4c1 1 2 2 1 4l-2 3c-2 2-5 2-8 1-8-3-15-10-18-18-1-3-1-6 1-8z" fill="#2f78a0"/>
      </svg>
      <span>15550148263</span>
    </div>
  </header>
  <div class="hero" role="img" aria-label="Stock photo of a hand using a calculator beside a laptop and a stethoscope"></div>
  <section class="greeting">
    <h1>Dear Alex,</h1>
    <p>Lorem ipsum dolor sit amet, consectetur adipiscing elit. Cras non semper lorem, vitae sagittis ante. Duis cursus consectetur sapien. Integer a urna vel urna varius viverra.</p>
    <div class="avatar" role="img" aria-label="Portrait of the sender">Image</div>
  </section>
  <section class="cards">
    <article class="card">
      <div class="card-image" role="img" aria-label="Article image">Image</div>
      <div class="card-body"><h2>Heading here</h2><p>Lorem ipsum dolor sit amet, consectetur adipiscing elit. Cras non semper lorem, vitae sagittis ante. Duis cursus consectetur sapien.</p><a class="button" href="#">Read more</a></div>
    </article>
    <article class="card">
      <div class="card-image" role="img" aria-label="Article image">Image</div>
      <div class="card-body"><h2>Heading here</h2><p>Lorem ipsum dolor sit amet, consectetur adipiscing elit. Cras non semper lorem, vitae sagittis ante. Duis cursus consectetur sapien.</p><a class="button" href="#">Read more</a></div>
    </article>
    <article class="card">
      <div class="card-image" role="img" aria-label="Article image">Image</div>
      <div class="card-body"><h2>Heading here</h2><p>Lorem ipsum dolor sit amet, consectetur adipiscing elit. Cras non semper lorem, vitae sagittis ante. Duis cursus consectetur sapien.</p><a class="button" href="#">Read more</a></div>
    </article>
    <article class="card">
      <div class="card-image" role="img" aria-label="Article image">Image</div>
      <div class="card-body"><h2>Heading here</h2><p>Lorem ipsum dolor sit amet, consectetur adipiscing elit. Cras non semper lorem, vitae sagittis ante. Duis cursus consectetur sapien.</p><a class="button" href="#">Read more</a></div>
    </article>
  </section>
  <section class="closing">
    <h2>Heading here</h2>
    <p>Lorem ipsum dolor sit amet, consectetur adipiscing elit. Cras non semper lorem, vitae sagittis ante. Duis cursus consectetur sapien. Integer a urna vel urna varius viverra. Phasellus eu libero in nibh viverra fringilla porttitor eget diam. Phasellus consectetur molestie nibh id cursus. Morbi tellus metus, pretium at ligula ut, pellentesque convallis enim.</p>
  </section>
</main>
<footer class="footer">
  <div class="footer-brand">
    <span class="footer-mark"></span>
    <span class="footer-name">Tavren Health Claims</span>
  </div>
  <div class="social" aria-label="Social links"><span></span><span></span><span></span><span></span></div>
  <p class="footer-text">Lorem ipsum dolor sit amet, consectetur adipiscing elit. Cras non semper lorem, vitae sagittis ante. Duis cursus consectetur sapien. Integer a urna vel urna varius viverra. Phasellus eu libero in nibh viverra fringilla porttitor eget diam. Phasellus consectetur molestie nibh id cursus. Morbi tellus metus, pretium at ligula.</p>
  <a class="unsubscribe" href="#">Unsubscribe</a>
</footer>
</body>
</html>
```